Redesign existing website.

I need a holidayhouse webdisain. Please review existing website: www.sorvimaja.ee
I want to keep my logo.
Target Market(s)
Nature and sea enjoying holidaymakers, aged 30 to 70
Requirements
Must have
- 3 languages (English, Russian and Estonian)

```html
<!DOCTYPE html>
<html lang="en">
<head>
<meta charset="utf-8">
<title>Sorvimaja Puhkemaja – About us</title>
<link href="https://fonts.googleapis.com/css2?family=Open+Sans:wght@400;600&display=swap" rel="stylesheet">
<style>
:root{
  --page:#fbf4ef;
  --white:#ffffff;
  --coral-top:#f3a283;
  --coral-bottom:#e96f55;
  --coral-edge:#c95a44;
  --accent:#e8704f;
  --sea:#0aa6e6;
  --meadow:#1e9a6a;
  --text:#666666;
  --muted:#777777;
  --footer:#2b2b2b;
  --footer-text:#b8b8b8;
  --icon:#8d8d8d;
}
*{margin:0;padding:0;box-sizing:border-box}
html,body{width:1200px;height:1179px;overflow:hidden}
body{position:relative;background:var(--page);font-family:"Open Sans",Arial,sans-serif;color:var(--text)}
.abs{position:absolute}

/* header */
.header-band{left:0;top:77px;width:1200px;height:64px;background:linear-gradient(100deg,var(--meadow) 0,var(--meadow) 190px,#8bc34a 200px,var(--sea) 212px,var(--sea) 100%)}
.header-bar{left:99px;top:34px;width:1002px;height:98px;border-radius:4px;background:linear-gradient(var(--coral-top),var(--coral-bottom));border-bottom:4px solid var(--coral-edge);box-shadow:0 2px 4px rgba(0,0,0,.15)}
.nav a{position:absolute;color:var(--white);text-decoration:none;font-size:14px;text-transform:uppercase;letter-spacing:.2px}
.nav a::before{content:"›";margin-right:9px}
.brand{left:540px;top:18px;width:120px;height:130px;display:flex;flex-direction:column;align-items:center;justify-content:center;gap:8px}
.brand-dot{width:56px;height:56px;border-radius:50%;background:var(--white)}
.brand-name{color:var(--white);font-size:14px;font-weight:600;letter-spacing:.5px}
.flags svg{position:absolute;top:72px;width:24px;height:17px}
.divider{left:892px;top:48px;width:1px;height:66px;background:rgba(255,255,255,.35)}
.call{right:99px;top:50px;text-align:right;color:var(--white)}
.call .label{font-size:17px;font-weight:600}
.call .number{font-size:22px;font-weight:600;margin-top:2px}

/* content */
.photo{left:103px;top:186px;width:311px;height:438px;background:linear-gradient(180deg,#7fb7ec 0%,#a8c8e6 30%,#b5704f 45%,#ddd8cc 65%,#6f8e3d 82%,#5a7a2c 100%)}
.about{left:436px;top:184px;width:656px}
.about h1{font-size:18px;font-weight:600;color:var(--accent);text-transform:uppercase;margin-bottom:3px}
.about p{font-size:13.4px;line-height:23px;margin-bottom:12px}

/* contact strip */
.contact{left:0;top:676px;width:1200px;height:93px;background:linear-gradient(var(--white),var(--white) 60%,#f6f6f6);border-top:1px solid #e8e0da}
.contact-item{position:absolute;display:flex;align-items:center;gap:14px;font-size:13.4px;line-height:23px;color:var(--muted)}
.contact-item svg{flex:none}

.map{left:0;top:769px;width:1195px;height:308px;background:linear-gradient(100deg,#a9cdf5 0%,#b8d7f4 35%,#e6ebe0 45%,#e2e8d8 70%,#d6e3c6 100%)}

/* footer */
.footer{left:0;top:1077px;width:1200px;height:102px;background:var(--footer)}
.footer-nav{left:101px;top:22px;font-size:13px;color:var(--footer-text);letter-spacing:.3px}
.footer-nav span.sep{margin:0 11px}
.copyright{left:101px;top:58px;font-size:13px;color:var(--footer-text);letter-spacing:.3px}
.social{top:50px;width:25px;height:25px;border-radius:50%;background:#5e5e5e}
</style>
</head>
<body>

<div class="abs header-band"></div>
<header class="abs header-bar">
  <nav class="nav">
    <a style="left:24px;top:18px">Home</a>
    <a style="left:24px;top:49px">About us</a>
    <a style="left:174px;top:18px">Price list</a>
    <a style="left:174px;top:49px">Location</a>
    <a style="left:331px;top:18px">Gallery</a>
    <a style="left:331px;top:49px">Picks</a>
  </nav>
</header>

<div class="abs brand">
  <span class="brand-dot"></span>
  <span class="brand-name">SORVIMAJA</span>
</div>

<div class="flags">
  <svg style="left:757px" viewBox="0 0 24 17" aria-label="English">
    <rect width="24" height="17" fill="#233a8c"/>
    <path d="M0 0L24 17M24 0L0 17" stroke="#fff" stroke-width="3"/>
    <path d="M0 0L24 17M24 0L0 17" stroke="#cc2233" stroke-width="1"/>
    <path d="M12 0V17M0 8.5H24" stroke="#fff" stroke-width="5"/>
    <path d="M12 0V17M0 8.5H24" stroke="#cc2233" stroke-width="3"/>
  </svg>
  <svg style="left:798px" viewBox="0 0 24 17" aria-label="Russian">
    <rect width="24" height="6" fill="#fff"/><rect y="6" width="24" height="5" fill="#1c3fa8"/><rect y="11" width="24" height="6" fill="#d52b1e"/>
  </svg>
  <svg style="left:840px" viewBox="0 0 24 17" aria-label="Estonian">
    <rect width="24" height="6" fill="#1f6fc8"/><rect y="6" width="24" height="5" fill="#111"/><rect y="11" width="24" height="6" fill="#fff"/>
  </svg>
</div>
<div class="abs divider"></div>
<div class="abs call">
  <div class="label">Call us</div>
  <div class="number">+372 55 12 3456</div>
</div>

<div class="abs photo" role="img" aria-label="Photo of the holiday cottage with a red tiled roof, terrace and garden lawn"></div>

<main class="abs about">
  <h1>About Sorvimaja Puhkemaja</h1>
  <p>Await a comfortable two-bedroom cottage. We are situated on the northern coast of the peninsula Juminda, Kaldaküla village Lahemaa National Park. Tallinn, just 61 km away. Kaldaküla is a suitable place for a cozy, relaxing setting. Iridescent sea and beautiful sunsets can be enjoyed even a house window.</p>
  <p>Curabitur lacinia neque et ante adipiscing, a semper nulla luctus. Vestibulum ligula purus, condimen­tum id nisl et, tempor vulputate lectus. Donec ac dapibus metus. Sed in pulvinar tellus, eu fringilla neque. Curabitur ut pellentesque sem. Class aptent taciti sociosqu ad litora torquent per conubia nostra, per inceptos himenaeos. Quisque id neque at felis varius pellentesque. Integer tincidunt id leo vel iaculis. Proin scelerisque leo a enim commodo eleifend ac eu tortor. In tempus elementum quam et placerat. Nullam molestie orci mauris, at gravida lorem scelerisque ut. Suspendisse laoreet nibh tellus, viverra mollis sem vestibulum quis. Curabitur tincidunt leo lorem, non rutrum metus rhoncus nec.</p>
  <p>Cras elementum ac felis vitae adipiscing. Etiam sit amet tortor felis. Morbi eget nisi eu nulla hendrerit euismod aliquet sed tortor. Vestibulum ante ipsum primis in faucibus orci luctus et ultrices posuere cubilia Curae; Suspendisse faucibus viverra velit sed iaculis. Nulla vitae consectetur lectus, a venenatis nisl. Phasellus sit amet condimentum nisl, quis fermentum nunc. Curabitur congue urna id libero hen­drerit, lobortis sagittis lorem blandit. Donec venenatis velit felis, id rhoncus nibh imperdiet nec. Cras in tristique enim. Maecenas diam lectus, viverra non ultricies non, mollis sit amet ante. Donec feugiat urna pretium tincidunt suscipit. Maecenas vel pretium diam. Nulla nec tempus libero.</p>
</main>

<section class="abs contact">
  <div class="contact-item" style="left:113px;top:24px">
    <svg width="24" height="28" viewBox="0 0 24 28"><rect x="1" y="1" width="22" height="26" fill="none" stroke="var(--icon)" stroke-width="2"/><path d="M7 3V13L10 10.5L13 13V3" fill="var(--icon)"/></svg>
    <span>Shore farm, Kaldaküla village<br>Rannametsa Parish, Harju 74999</span>
  </div>
  <div class="contact-item" style="left:403px;top:35px">
    <svg width="28" height="28" viewBox="0 0 28 28"><path d="M3 5L8 1L13 8L10 11C11 14 14 17 17 18L20 15L27 20L23 25C13 25 3 15 3 5Z" fill="var(--icon)"/></svg>
    <span>Phone: +372 55 12 3456</span>
  </div>
  <div class="contact-item" style="left:655px;top:34px">
    <svg width="30" height="28" viewBox="0 0 30 28"><rect x="1" y="8" width="7" height="19" fill="var(--icon)"/><rect x="10" y="1" width="12" height="8" fill="none" stroke="var(--icon)" stroke-width="2"/><rect x="9" y="10" width="20" height="17" fill="var(--icon)"/><g fill="#fff"><rect x="13" y="14" width="3" height="2"/><rect x="18" y="14" width="3" height="2"/><rect x="23" y="14" width="3" height="2"/><rect x="13" y="18" width="3" height="2"/><rect x="18" y="18" width="3" height="2"/><rect x="23" y="18" width="3" height="2"/><rect x="13" y="22" width="3" height="2"/><rect x="18" y="22" width="3" height="2"/><rect x="23" y="22" width="3" height="2"/></g></svg>
    <span>Fax : +372 55 12 3456</span>
  </div>
  <div class="contact-item" style="left:883px;top:35px">
    <svg width="28" height="20" viewBox="0 0 28 20"><rect width="28" height="20" fill="var(--icon)"/><path d="M1 1L14 11L27 1" fill="none" stroke="#fff" stroke-width="1.5"/></svg>
    <span>E-mail : info@sorvimaja.ee</span>
  </div>
</section>

<div class="abs map" role="img" aria-label="Road map of the northern Estonian coast from Tallinn towards Lahemaa, showing the way to the cottage"></div>

<footer class="abs footer">
  <div class="abs footer-nav">Home<span class="sep">|</span>About us<span class="sep">|</span>Price list<span class="sep">|</span>Locations<span class="sep">|</span>Gallery<span class="sep">|</span>Picks<span class="sep">|</span>Contact us</div>
  <div class="abs copyright">Copyright &nbsp;©&nbsp; 2014 &nbsp; Sorvimaja. &nbsp; All rights reserved.</div>
  <span class="abs social" style="left:970px"></span>
  <span class="abs social" style="left:1005px"></span>
  <span class="abs social" style="left:1040px"></span>
  <svg class="abs social" style="left:1074px" viewBox="0 0 25 25"><path d="M7 8H18V17H7Z" fill="none" stroke="#ccc" stroke-width="1.4"/><path d="M7 8L12.5 13L18 8" fill="none" stroke="#ccc" stroke-width="1.4"/></svg>
</footer>

</body>
</html>
```